Visitenkarten-Design für Anbieter von Softwarelösungen rund ums Bargeld
Unser Favorit war gleich beim 1. Entwurf mit dabei. Schön war vor allem, dass uns gleich 3 verschiedene Farbvarianten angeboten wurden. Daher bedurfte es auch keinerlei Anpassungen von unserer Seite. Herzlichen Dank!
Zielgruppe
Unsere Unternehmensgruppe, bestehend aus mehreren Tochterunternehmen, ist ein führender europäischer Anbieter für Softwarelösungen rund ums Bargeld.
Unsere Lösungen unterstützen Handelsunternehmen, Wertdienstleister und Finanzinstitute bei der Erfassung und Nachverfolgung von Zahlungsströmen im Bargeldkreislauf (Cash Management + Track & Trace). Bargeldmanagementprozesse werden durch unsere Produkte bei unseren Kunden optimiert, Verwaltungs-, Prozess- und Personalkosten gesenkt: Für mehr Sicherheit, Effizienz und Transparenz.
Es ist wahrscheinlich, dass wir zukünftig mittels Zukäufen über unsere derzeitigen Tätigkeitsfelder hinaus wachsen. Neben Cash wird die (Werte-)Logistik bzw. Logistik generell eine Rolle spielen. Auch unter der Maßgabe, dass zukünftig nur noch Services (statt Verkauf von Software) angeboten werden.
Der Fokus wird sich weiterhin primär auf Geschäftskunden beschränken: Wir helfen Unternehmen, effizienter zu werden.
www.digital.korven-beispiel.eu
Aufgabenstellung
Die Schreibweise unseres Namens sieht wie folgt aus: 'KORVEN | Digital Solutions'
Die Farbcodes des Logo sind in der Datei abgebildet.
Als ergänzende Farben nutzen wir aktuell ein Türkis (CMYK: 53/23/21/0 | #86ACBA) und ein Dunkelgrau (CMYK: 77/62/38/21 | #44546A). Diese dürfen gerne mit verwendet werden.

```html
<!DOCTYPE html>
<html lang="de">
<head>
<meta charset="utf-8">
<title>KORVEN Digital Solutions – Visitenkarten</title>
<link href="https://fonts.googleapis.com/css2?family=Raleway:wght@400;600;700;800&display=swap" rel="stylesheet">
<style>
  :root {
    --backdrop: #b0b2b1;
    --card-white: #ffffff;
    --brand-red: #7f1729;
    --brand-navy: #44546a;
    --text-grey: #555a5f;
    --deco-light: #f1f2f2;
    --deco-on-dark: rgba(255,255,255,0.08);
    --divider: #b9babb;
  }
  * { box-sizing: border-box; margin: 0; padding: 0; }
  html, body { width: 1200px; height: 1200px; overflow: hidden; }
  body {
    background: var(--backdrop);
    font-family: "Raleway", sans-serif;
    position: relative;
  }
  .card {
    position: absolute;
    width: 408px;
    height: 264px;
    overflow: hidden;
    background: var(--card-white);
  }
  .card--front { left: 96px; }
  .card--back { left: 696px; }
  .row-1 { top: 96px; }
  .row-2 { top: 468px; }
  .row-3 { top: 840px; }
  .card--red { background: var(--brand-red); }
  .card--navy { background: var(--brand-navy); }

  .deco-ring {
    position: absolute;
    border-radius: 50%;
    border: 16px solid var(--deco-light);
    width: 290px; height: 290px; top: -15px;
  }
  .card--front .deco-ring { left: 250px; }
  .card--red .deco-ring, .card--navy .deco-ring { border-color: var(--deco-on-dark); }
  .card--back .deco-ring { left: -130px; }

  /* front wordmark */
  .wordmark {
    position: absolute;
    left: 40px;
    top: 107px;
    display: flex;
    align-items: center;
    color: var(--brand-red);
  }
  .card--red .wordmark, .card--navy .wordmark { color: var(--card-white); }
  .wordmark__dot {
    width: 40px; height: 40px;
    border-radius: 50%;
    border: 3px solid currentColor;
  }
  .wordmark__rule {
    width: 1px; height: 50px;
    background: currentColor;
    margin: 0 12px 0 14px;
    opacity: 0.6;
  }
  .wordmark__name { font-weight: 700; line-height: 1; }
  .wordmark__name-main { display: block; font-size: 30px; letter-spacing: 0.5px; }
  .wordmark__name-sub { display: block; font-size: 11.5px; letter-spacing: 0.6px; margin-top: 2px; }

  /* back */
  .back__mark {
    position: absolute;
    left: 334px; top: 22px;
    width: 40px; height: 40px;
    border-radius: 50%;
    border: 3px solid var(--brand-red);
  }
  .person {
    position: absolute;
    left: 47px; top: 96px;
    font-size: 13px;
    line-height: 17px;
    color: var(--text-grey);
    white-space: nowrap;
  }
  .person__name, .company__name {
    color: var(--brand-red);
    font-weight: 600;
  }
  .back__divider {
    position: absolute;
    left: 188px; top: 96px;
    width: 1px; height: 146px;
    background: var(--divider);
  }
  .company {
    position: absolute;
    left: 202px; top: 96px;
    font-size: 13px;
    line-height: 17px;
    color: var(--text-grey);
    white-space: nowrap;
  }
  .company__name span { color: var(--text-grey); }
  .contact-list {
    list-style: none;
    margin-top: 9px;
    font-size: 12.5px;
  }
  .contact-list li {
    display: flex;
    align-items: center;
    height: 17px;
    white-space: nowrap;
  }
  .contact-list svg {
    width: 12px; height: 12px;
    margin-right: 10px;
    fill: var(--brand-red);
    flex: none;
  }
</style>
</head>
<body>

<section class="card card--front row-1">
  <div class="deco-ring"></div>
  <div class="wordmark">
    <div class="wordmark__dot"></div>
    <div class="wordmark__rule"></div>
    <div class="wordmark__name">
      <span class="wordmark__name-main">KORVEN</span>
      <span class="wordmark__name-sub">DIGITAL SOLUTIONS</span>
    </div>
  </div>
</section>

<section class="card card--back row-1">
  <div class="deco-ring"></div>
  <div class="back__mark"></div>
  <div class="person">
    <div class="person__name">Jonas Weidlich</div>
    <div>Managing Director</div>
  </div>
  <div class="back__divider"></div>
  <div class="company">
    <div class="company__name">KORVEN <span>Digital Solutions</span></div>
    <div>Birkenallee 7</div>
    <div>04177 Musterstadt</div>
    <div>Germany</div>
    <ul class="contact-list">
      <li><svg viewBox="0 0 12 12"><path d="M2 11 C1 8 3 3 8 1.5 L10 1 L10.5 3.5 L8 4.2 C6 5 4.5 7 4.3 9.5 L4.5 11 Z"/></svg>+49 341 555012-00</li>
      <li><svg viewBox="0 0 12 12"><path d="M3 1h6v3H3z M1 4.5h10v5H9V8H3v1.5H1z M3.5 8.8h5V11h-5z"/></svg>+49 341 555012-89</li>
      <li><svg viewBox="0 0 12 12"><path d="M0.5 2.5h11v7h-11z M1 3l5 3.5L11 3" fill="none" stroke="#7f1729" stroke-width="1.3"/></svg>info@korven.example</li>
      <li><svg viewBox="0 0 12 12"><circle cx="6" cy="6" r="5" fill="none" stroke="#7f1729" stroke-width="1.4"/><path d="M1 6h10 M6 1c-3 3-3 7 0 10 M6 1c3 3 3 7 0 10" fill="none" stroke="#7f1729" stroke-width="1"/></svg>www.digital.korven-beispiel.eu</li>
    </ul>
  </div>
</section>

<section class="card card--front card--red row-2">
  <div class="deco-ring"></div>
  <div class="wordmark">
    <div class="wordmark__dot"></div>
    <div class="wordmark__rule"></div>
    <div class="wordmark__name">
      <span class="wordmark__name-main">KORVEN</span>
      <span class="wordmark__name-sub">DIGITAL SOLUTIONS</span>
    </div>
  </div>
</section>

<section class="card card--back row-2">
  <div class="deco-ring"></div>
  <div class="back__mark"></div>
  <div class="person">
    <div class="person__name">Jonas Weidlich</div>
    <div>Managing Director</div>
  </div>
  <div class="back__divider"></div>
  <div class="company">
    <div class="company__name">KORVEN <span>Digital Solutions</span></div>
    <div>Birkenallee 7</div>
    <div>04177 Musterstadt</div>
    <div>Germany</div>
    <ul class="contact-list">
      <li><svg viewBox="0 0 12 12"><path d="M2 11 C1 8 3 3 8 1.5 L10 1 L10.5 3.5 L8 4.2 C6 5 4.5 7 4.3 9.5 L4.5 11 Z"/></svg>+49 341 555012-00</li>
      <li><svg viewBox="0 0 12 12"><path d="M3 1h6v3H3z M1 4.5h10v5H9V8H3v1.5H1z M3.5 8.8h5V11h-5z"/></svg>+49 341 555012-89</li>
      <li><svg viewBox="0 0 12 12"><path d="M0.5 2.5h11v7h-11z M1 3l5 3.5L11 3" fill="none" stroke="#7f1729" stroke-width="1.3"/></svg>info@korven.example</li>
      <li><svg viewBox="0 0 12 12"><circle cx="6" cy="6" r="5" fill="none" stroke="#7f1729" stroke-width="1.4"/><path d="M1 6h10 M6 1c-3 3-3 7 0 10 M6 1c3 3 3 7 0 10" fill="none" stroke="#7f1729" stroke-width="1"/></svg>www.digital.korven-beispiel.eu</li>
    </ul>
  </div>
</section>

<section class="card card--front card--navy row-3">
  <div class="deco-ring"></div>
  <div class="wordmark">
    <div class="wordmark__dot"></div>
    <div class="wordmark__rule"></div>
    <div class="wordmark__name">
      <span class="wordmark__name-main">KORVEN</span>
      <span class="wordmark__name-sub">DIGITAL SOLUTIONS</span>
    </div>
  </div>
</section>

<section class="card card--back row-3">
  <div class="deco-ring"></div>
  <div class="back__mark"></div>
  <div class="person">
    <div class="person__name">Jonas Weidlich</div>
    <div>Managing Director</div>
  </div>
  <div class="back__divider"></div>
  <div class="company">
    <div class="company__name">KORVEN <span>Digital Solutions</span></div>
    <div>Birkenallee 7</div>
    <div>04177 Musterstadt</div>
    <div>Germany</div>
    <ul class="contact-list">
      <li><svg viewBox="0 0 12 12"><path d="M2 11 C1 8 3 3 8 1.5 L10 1 L10.5 3.5 L8 4.2 C6 5 4.5 7 4.3 9.5 L4.5 11 Z"/></svg>+49 341 555012-00</li>
      <li><svg viewBox="0 0 12 12"><path d="M3 1h6v3H3z M1 4.5h10v5H9V8H3v1.5H1z M3.5 8.8h5V11h-5z"/></svg>+49 341 555012-89</li>
      <li><svg viewBox="0 0 12 12"><path d="M0.5 2.5h11v7h-11z M1 3l5 3.5L11 3" fill="none" stroke="#7f1729" stroke-width="1.3"/></svg>info@korven.example</li>
      <li><svg viewBox="0 0 12 12"><circle cx="6" cy="6" r="5" fill="none" stroke="#7f1729" stroke-width="1.4"/><path d="M1 6h10 M6 1c-3 3-3 7 0 10 M6 1c3 3 3 7 0 10" fill="none" stroke="#7f1729" stroke-width="1"/></svg>www.digital.korven-beispiel.eu</li>
    </ul>
  </div>
</section>

</body>
</html>
```